Driftwater

Club flyer, grand opening night, house/electronic music, looking for clean design with a sample image attached. Please look at the prior flyers to get an idea of the style. Guaranteed project
I would like to use the red design if possible (driftwater flyer attached)
Text:
DRIFTWATER
Winter House Music Monthly
Opening Night Dec 13 2013
Tessaline (use logo)
Featuring
BRONTIK (House/Garage)
(use logo with just Brontik name)
w/ resident
ZEV (Pinwheel)
Free All Night
Target Market(s)
21-39 year old club with all house/electronic music. classier and grown up over gimmicky
Industry/Entity Type
Club
Look and feel

```html
<!DOCTYPE html>
<html lang="en">
<head>
<meta charset="utf-8">
<title>Driftwater – Winter House Music Monthly</title>
<link href="https://fonts.googleapis.com/css2?family=Source+Sans+3:wght@400;600;700&display=swap" rel="stylesheet">
<style>
  :root {
    --page-bg: #e4e4e4;
    --maroon-deep: #3b0718;
    --maroon: #5c1030;
    --maroon-mid: #7a1a3c;
    --glow-orange: #e8672e;
    --glow-rose: #c23a55;
    --strip: #460a1f;
    --band: #f1f2f6;
    --white: #ffffff;
    --pink: #e8236e;
    --ribbon: #4a4a4c;
    --ribbon-edge: #2c2c2e;
    --mark: #c8455f;
  }
  * { box-sizing: border-box; margin: 0; padding: 0; }
  html, body {
    width: 1200px;
    height: 900px;
    overflow: hidden;
    background: var(--page-bg);
    font-family: "Source Sans 3", "Myriad Pro", Arial, sans-serif;
  }
  .flyer {
    position: absolute;
    left: 310px;
    top: 40px;
    width: 580px;
    height: 820px;
    background: var(--strip);
    box-shadow: 0 6px 18px rgba(0, 0, 0, 0.35);
    overflow: hidden;
  }
  .flyer__scene {
    position: absolute;
    inset: 0 0 165px 0;
    background:
      radial-gradient(ellipse 38% 22% at 50% 34%, rgba(255, 190, 120, 0.55), transparent 70%),
      radial-gradient(ellipse 70% 40% at 48% 32%, var(--glow-orange) 0%, var(--glow-rose) 35%, transparent 75%),
      linear-gradient(180deg, var(--maroon) 0%, var(--maroon-mid) 30%, var(--maroon) 55%, var(--maroon-deep) 100%);
  }
  .flyer__headliner {
    position: absolute;
    top: 50px;
    right: 50px;
    color: var(--white);
    font-size: 30px;
    font-weight: 700;
    letter-spacing: 2px;
  }
  .flyer__tag {
    position: absolute;
    top: 136px;
    left: 0;
    width: 191px;
    height: 39px;
    padding-left: 26px;
    line-height: 39px;
    color: var(--white);
    font-size: 20px;
    font-weight: 600;
    background: var(--ribbon);
    border-bottom: 3px solid var(--ribbon-edge);
    clip-path: polygon(0 0, 100% 0, 94% 50%, 100% 100%, 0 100%);
  }
  .flyer__titles {
    position: absolute;
    top: 436px;
    left: 0;
    width: 100%;
    text-align: center;
    color: var(--white);
  }
  .flyer__title {
    font-size: 54px;
    font-weight: 600;
    line-height: 1;
    letter-spacing: 0.5px;
  }
  .flyer__subtitle {
    margin-top: 10px;
    color: var(--pink);
    font-size: 17px;
    font-weight: 600;
  }
  .flyer__date {
    margin-top: 76px;
    font-size: 23px;
    font-weight: 700;
  }
  .flyer__partners {
    position: absolute;
    top: 655px;
    left: 0;
    width: 100%;
    height: 120px;
    background: var(--band);
    display: flex;
    flex-direction: column;
    align-items: center;
    justify-content: center;
    gap: 8px;
    color: var(--mark);
    font-weight: 600;
  }
  .flyer__partner--venue { font-size: 18px; letter-spacing: 1px; }
  .flyer__partner--resident { font-size: 28px; letter-spacing: 3px; }
</style>
</head>
<body>
  <main class="flyer">
    <div class="flyer__scene" role="img" aria-label="Club crowd silhouettes with raised hands under warm stage lights, light rays and bokeh"></div>
    <div class="flyer__headliner">BRONTIK</div>
    <div class="flyer__tag">Free All Night</div>
    <div class="flyer__titles">
      <h1 class="flyer__title">DRIFTWATER</h1>
      <p class="flyer__subtitle">WINTER HOUSE MUSIC MONTHLY</p>
      <p class="flyer__date">OPENING NIGHT DEC 13 2013</p>
    </div>
    <div class="flyer__partners">
      <span class="flyer__partner--venue">TESSALINE</span>
      <span class="flyer__partner--resident">PINWHEEL</span>
    </div>
  </main>
</body>
</html>
```